I need a Professional Eye-Catching Paperback and e-Book Cover Design done with different mockups

I need a Professional Eye-Catching e-Book Cover Design done with different mockups

I need 2-3 designs to choose from per designer.

Book title - Lasting Harvest:

Subtitle - Growing riches beyond your years

Author name - K. Dapo Ramiro

I have attached some sample designs but i need you to be creative.

```html
<!DOCTYPE html>
<html lang="en">
<head>
<meta charset="utf-8">
<title>Lasting Harvest — Cover</title>
<link href="https://fonts.googleapis.com/css2?family=Anton&family=Archivo:ital,wdth,wght@0,100,800;1,125,900&display=swap" rel="stylesheet">
<style>
  :root {
    --backdrop: #e4e4e4;
    --cream: #fdfbd0;
    --sky: #7fa6b8;
    --sky-deep: #5d8aa0;
    --sun: #fffbe6;
    --glow: #f6dc93;
    --stone: #3b3629;
    --stone-dark: #23201a;
    --root-gold: #8d6c36;
    --shadow: rgba(20, 16, 8, 0.45);
  }
  * { margin: 0; padding: 0; box-sizing: border-box; }
  html, body {
    width: 1200px;
    height: 925px;
    overflow: hidden;
    background: var(--backdrop);
  }
  .canvas {
    position: relative;
    width: 1200px;
    height: 925px;
  }
  .cover {
    position: absolute;
    left: 292px;
    top: 0;
    width: 616px;
    height: 925px;
    overflow: hidden;
  }
  .cover-art {
    position: absolute;
    inset: 0;
    background:
      radial-gradient(circle at 50% 11%, var(--sun) 0, var(--glow) 7%, rgba(246,220,147,0.35) 22%, rgba(246,220,147,0) 42%),
      linear-gradient(180deg, var(--sky-deep) 0%, var(--sky) 25%, #9a9170 40%, var(--stone) 55%, var(--stone-dark) 72%, var(--root-gold) 86%, #4a3a22 100%);
  }
  .title-block {
    position: absolute;
    inset: 0;
    color: var(--cream);
    text-align: center;
    text-shadow: 0 2px 6px var(--shadow);
  }
  .title {
    position: absolute;
    left: 0;
    width: 100%;
    font-family: 'Anton', 'Impact', sans-serif;
    font-weight: 400;
    text-transform: uppercase;
    line-height: 1;
  }
  .title-line-1 {
    top: 424px;
    font-size: 70px;
    letter-spacing: 1px;
    transform: rotate(-2deg);
  }
  .title-line-2 {
    top: 488px;
    font-size: 84px;
    letter-spacing: 1px;
    transform: rotate(-1deg);
  }
  .subtitle {
    position: absolute;
    left: 0;
    width: 100%;
    font-family: 'Archivo', 'Arial Black', sans-serif;
    font-style: italic;
    font-weight: 900;
    font-stretch: 125%;
    text-transform: uppercase;
    line-height: 1;
  }
  .subtitle-top {
    top: 618px;
    font-size: 31px;
    transform: rotate(2deg);
  }
  .subtitle-bottom {
    top: 692px;
    font-size: 38px;
    letter-spacing: -1px;
  }
  .rule-label {
    position: absolute;
    display: flex;
    align-items: center;
    gap: 12px;
    font-family: 'Archivo', 'Arial', sans-serif;
    font-weight: 800;
    font-stretch: 100%;
    text-transform: uppercase;
    letter-spacing: 6px;
    color: var(--cream);
  }
  .rule-label::before,
  .rule-label::after {
    content: "";
    flex: 1;
    height: 2px;
    background: var(--cream);
  }
  .rule-middle {
    left: 110px;
    width: 398px;
    top: 656px;
    font-size: 19px;
  }
  .rule-by {
    left: 187px;
    width: 244px;
    top: 802px;
    font-size: 15px;
  }
  .author {
    position: absolute;
    left: 0;
    width: 100%;
    top: 826px;
    font-family: 'Archivo', 'Arial', sans-serif;
    font-weight: 800;
    font-stretch: 100%;
    font-size: 33px;
    letter-spacing: -0.5px;
    color: var(--cream);
    text-align: center;
    text-shadow: 0 2px 6px var(--shadow);
  }
</style>
</head>
<body>
  <main class="canvas">
    <section class="cover">
      <div class="cover-art" role="img" aria-label="Ancient stone temple rising into a sunburst sky with clouds, its base gripped by sprawling golden tree roots"></div>
      <div class="title-block">
        <h1>
          <span class="title title-line-1">Lasting</span>
          <span class="title title-line-2">Harvest:</span>
        </h1>
        <p class="subtitle subtitle-top">Growing Riches</p>
        <p class="rule-label rule-middle">Beyond</p>
        <p class="subtitle subtitle-bottom">Your Years</p>
        <p class="rule-label rule-by">By</p>
        <p class="author">K. Dapo Ramiro</p>
      </div>
    </section>
  </main>
</body>
</html>
```